Web Design Project

Need a web design for a website that provides senior corporate executives with leadership assessment and improvement guidance. The homepage has two purposes- 1) place for users to log in (primary purpose), and 2) marketing of the site.

The company is named Beacon 720, and it provides 360 degree leadership assessments for senior executives. In a nutshell, that means a person's co-workers, employees, customers, and bosses fill out a survey on how well the person does his or her job; and we tell him how well he or she is doing and how to improve.

The attached logo (360_logo) should serve as the inspiration for colors, and the website must use the logo. The homepage will mostly be used for logging in, so it should be simple, clean, and professional looking. See attached sketch.pdf for what we have in mind. The sketch is provided merely to give insight. We're not married to it. All text can be latinized jibberish in the design.

There is one important size constraint to keep in mind. The attached file (content_dimensions.pdf) specifies a content area that must be (width x height) 850 x 600 px.

Note that sketch.pdf portrays images, but please note these are merely placeholders. We will use screenshots of our application on the homepage, so any images you use in content area should be examples or suggestions.
Updates

Target Market(s)

Senior business executives from large companies in the manufacturing and energy sectors. Typically males aged 25 and older, white collar, upper class, with advanced degrees in business, engineering, and natural sciences.

Industry/Entity Type

It Company

Requirements
Must have
• See content_dimensions.pdf, which specifies the dimensions of the content area (850x600 px) (w x h). The the gutter and sides can expand beyond that, but the content area must be that specific size.

Note: The login panel must be within the content area.

Must use the attached logo (360_logo.png).
Should not have
• No Flash and no animated gifs. No photos of people.

```html
<!DOCTYPE html>
<html lang="en">
<head>
<meta charset="utf-8">
<title>Beacon 720 — Leadership Assessment</title>
<link rel="stylesheet" href="https://fonts.googleapis.com/css2?family=Questrial&family=Roboto:wght@300&display=swap">
<style>
  :root {
    --green: #9dca3c;
    --orange: #f7941d;
    --blue: #1d5d8e;
    --ink: #333333;
    --text: #444444;
    --muted: #888888;
    --line: #cfcfcf;
    --white: #ffffff;
    --panel-fade: #ececec;
  }
  * { margin: 0; padding: 0; box-sizing: border-box; }
  html, body { width: 1200px; height: 795px; overflow: hidden; background: var(--white); }
  body { position: relative; font-family: "Questrial", sans-serif; color: var(--text); }
  h1, h2 { font-weight: 400; }
  .abs { position: absolute; }

  .header-band { left: 237px; top: 115px; width: 72px; height: 35px; background: var(--green); }
  .brand-name { left: 309px; top: 115px; width: 138px; height: 35px; line-height: 35px; text-align: center;
    font-size: 19px; color: var(--orange); white-space: nowrap; }

  .main-nav { left: 447px; top: 115px; width: 517px; height: 35px; background: var(--green); }
  .main-nav a { position: absolute; top: 0; line-height: 35px; color: var(--white); font-size: 18px; text-decoration: none; letter-spacing: -0.3px; }
  .nav-divider { position: absolute; top: 10px; height: 16px; border-left: 1px dotted rgba(255,255,255,.8); }

  .panel { top: 166px; height: 514px; border: 1px solid var(--line);
    background: linear-gradient(to bottom, var(--white) 0%, var(--white) 80%, var(--panel-fade) 100%); }
  .login-panel { left: 237px; width: 230px; }
  .content-panel { left: 472px; width: 492px; }

  .login-title { left: 254px; top: 186px; width: 199px; height: 28px; background: var(--orange);
    color: var(--white); font-size: 18px; padding: 3px 11px; }
  .login-field { left: 254px; width: 199px; height: 29px; border: 1px solid var(--line);
    font-family: "Questrial", sans-serif; font-size: 11px; color: var(--muted); padding: 0 13px; background: var(--white); }
  .login-field::placeholder { color: #999; }
  .login-button { left: 375px; top: 293px; width: 78px; height: 26px; border: none;
    background: repeating-linear-gradient(135deg, var(--blue) 0 2px, #2a6b9c 2px 4px);
    color: var(--white); font-family: "Questrial", sans-serif; font-size: 16px; }

  .lead-title { left: 497px; top: 191px; font-size: 18px; color: #555; letter-spacing: -0.2px; white-space: nowrap; }
  .lead-sub { left: 497px; top: 213px; font-size: 12.5px; color: var(--orange); white-space: nowrap; }
  .body-copy { font-size: 11px; line-height: 15.4px; color: var(--ink); }
  .copy-a { left: 497px; top: 243px; width: 218px; }
  .copy-b { left: 497px; top: 318px; width: 218px; line-height: 13.4px; }

  .globe-art { left: 763px; top: 243px; width: 173px; height: 151px; border-radius: 50%;
    background: radial-gradient(circle at 45% 45%, #e3ebf3 0%, #b9cfe0 55%, #eef3f7 100%); }

  .feature-title { left: 497px; top: 414px; font-size: 15px; color: var(--ink); white-space: nowrap; }
  .feature-sub { left: 497px; top: 435px; font-size: 10.5px; color: var(--orange); white-space: nowrap; }
  .copy-c { left: 497px; top: 453px; width: 445px; line-height: 13px; color: #555; }

  .chart-art { left: 507px; top: 504px; width: 183px; height: 154px; border-radius: 6px;
    background: linear-gradient(120deg, #7fbf3f 0%, #f2c94c 45%, #f29a3a 70%, #e7e7e7 100%); }
  .column-divider { left: 716px; top: 509px; height: 144px; border-left: 1px dotted #999; }
  .aside-title { left: 735px; top: 508px; width: 215px; font-size: 15px; line-height: 18px; color: var(--ink); }
  .copy-d { left: 735px; top: 559px; width: 210px; line-height: 14.4px; color: #555; }

  .copyright { left: 237px; top: 696px; font-family: "Roboto", sans-serif; font-weight: 300; font-size: 11px; color: #777; }
  .footer-brand { left: 840px; top: 691px; width: 124px; text-align: right; font-size: 19px; color: var(--orange); white-space: nowrap; }
</style>
</head>
<body>
  <div class="abs header-band"></div>
  <div class="abs brand-name">Beacon 720</div>

  <nav class="abs main-nav">
    <a href="#" style="left:44px">ABOUT</a>
    <span class="nav-divider" style="left:143px"></span>
    <a href="#" style="left:171px">FAQ</a>
    <span class="nav-divider" style="left:243px"></span>
    <a href="#" style="left:280px">HELP</a>
    <span class="nav-divider" style="left:347px"></span>
    <a href="#" style="left:374px">CONTACT</a>
  </nav>

  <div class="abs panel login-panel"></div>
  <div class="abs panel content-panel"></div>

  <div class="abs login-title">Login</div>
  <input class="abs login-field" style="top:220px" type="text" placeholder="Enter Your Login Name">
  <input class="abs login-field" style="top:256px" type="password" placeholder="Enter Your Password">
  <button class="abs login-button" type="button">Login</button>

  <h1 class="abs lead-title">PROVIDES SENIOR CORPORATE EXECUTIVES</h1>
  <p class="abs lead-sub">With Leadership Assessment And Improvement Guidance</p>
  <p class="abs body-copy copy-a">Lorem ipsum dolor sit amet, consectetuer adipiscing elit, sed diam nonummy nibh euismod tincidunt ut laoreet dolore magna aliquam erat volutpat.</p>
  <p class="abs body-copy copy-b">Ut wisi enim ad minim veniam, quis nostrud exerci tation ullamcorper suscipit lobortis nisl ut aliquip ex ea commodo consequat. Duis autem vel eum iriure dolor in hendrerit in vulputate velit esse molestie consequat, vel illum dolore eu.</p>
  <div class="abs globe-art" role="img" aria-label="Sphere made of pale blue tiles"></div>

  <h2 class="abs feature-title">Lorem ipsum dolor sit amet, consectetuer adipiscing elit</h2>
  <p class="abs feature-sub">sed diam nonummy nibh euismod tincidunt ut laoreet dolore</p>
  <p class="abs body-copy copy-c">Ut wisi enim ad minim veniam, quis nostrud exerci tation ullamcorper suscipit lobortis nisl ut aliquip ex ea commodo consequat.</p>

  <div class="abs chart-art" role="img" aria-label="3D growth chart with coloured bars and a rising green arrow on a disc"></div>
  <div class="abs column-divider"></div>
  <h2 class="abs aside-title">Lorem ipsum dolor sit amet, consectetuer adipiscing elit</h2>
  <p class="abs body-copy copy-d">Ut wisi enim ad minim veniam, quis nostrud exerci tation ullamcorper suscipit lobortis nisl ut aliquip ex ea commodo consequat. Duis autem vel eum iriure dolor in hendrerit in vulputate velit esse molestie consequat, vel illum dolore eu.</p>

  <p class="abs copyright">© Copyright 2013 Beacon 720. All rights reserved.</p>
  <div class="abs footer-brand">Beacon 720</div>
</body>
</html>
```